Barrister Letterhead incorporating existing logo/design

Require new letterhead template to incorporate logo and information on 'Letter 2015' word document. Currently the information on the letterhead is very busy and would like a cleaner look.
Must look good in black and white, and colour when printed.

Target Market(s)

Professional

Industry/Entity Type

Legal

Requirements
Must have
• Clean professional look.

```html
<!DOCTYPE html>
<html lang="en">
<head>
<meta charset="utf-8">
<title>Harlow Chambers Letterhead</title>
<link rel="stylesheet" href="https://fonts.googleapis.com/css2?family=Cormorant+Garamond:wght@500;600&display=swap">
<style>
  :root {
    --navy: #1b2a47;
    --grey: #a0a0a0;
    --rule: #b5b5b5;
    --paper: #ffffff;
  }
  html, body {
    margin: 0;
    padding: 0;
    width: 1200px;
    height: 1000px;
    overflow: hidden;
    background: var(--paper);
  }
  .letterhead {
    position: relative;
    width: 1200px;
    height: 1000px;
    font-family: "Cormorant Garamond", Georgia, serif;
    color: var(--navy);
  }
  .masthead {
    position: absolute;
    left: 0;
    top: 0;
    width: 1200px;
    height: 300px;
  }
  .masthead .firm-name {
    font-family: "Cormorant Garamond", Georgia, serif;
    font-weight: 600;
    font-size: 84px;
    fill: var(--navy);
  }
  .masthead .tagline {
    font-family: "Cormorant Garamond", Georgia, serif;
    font-weight: 500;
    font-size: 66px;
    fill: var(--grey);
  }
  .masthead .mark { fill: var(--navy); }
  .masthead .divider { stroke: var(--rule); stroke-width: 1.2; }
  .contact {
    position: absolute;
    left: 0;
    top: 303px;
    width: 1200px;
    margin: 0;
    padding: 0;
    list-style: none;
    text-align: center;
    font-weight: 500;
    font-size: 47px;
    line-height: 58.5px;
    text-transform: uppercase;
    letter-spacing: 0.2px;
  }
  .contact li { margin: 0; }
  .contact .fax { padding-right: 80px; }
</style>
</head>
<body>
  <main class="letterhead">
    <svg class="masthead" width="1200" height="300" viewBox="0 0 1200 300" aria-label="Harlow Chambers, Barristers and Mediators">
      <rect class="mark" x="100" y="136" width="155" height="155"/>
      <text class="firm-name" x="283" y="200" textLength="835" lengthAdjust="spacingAndGlyphs">HARLOW CHAMBERS</text>
      <line class="divider" x1="283" y1="224" x2="1118" y2="224"/>
      <text class="tagline" x="283" y="285" textLength="832" lengthAdjust="spacing">Barristers and Mediators</text>
    </svg>
    <ul class="contact">
      <li class="street">Level 1 42 Marlin Street, Kestrelton</li>
      <li class="postal">P.O. Box 218, Kestrelton. Q. 4900</li>
      <li class="phone">Telephone 07 4000 1234</li>
      <li class="fax">Fax 07 4000 5678</li>
      <li class="email">Email jmoss@examplebar.asn.au</li>
      <li class="web">www.harlowchambers.com.au</li>
    </ul>
  </main>
</body>
</html>
```